Graphic background for 10 Pull Up Banners

To produce a graphic background for a 100 cm wide by 200 cm high Pull-Up Display banner containing a Buddhist text in three languages: Tibetan, Mandarin and English. Please refer to uploaded file "Elements of Pull Up Banner". The design should be simple (not drawing attention away from the text). This design should then be varied for or extended to the next banner and so on until the 10th banner. When the banners are lined up, they should form a single design that is 1000 cm wide by 200 cm high.
An alternative way to look at the project is to produce a graphic background of 1000 cm width by 200 cm height that is then splitted into ten separate 100 cm wide by 200 cm high graphic to be used as background for 10 Buddhist texts (text 1, 2, 3, 4, 5, 6, 7, 8, 9a, 9b) on 10 Pull-Up Display Banners, the text in each banner being in the three languages mentioned earlier.
In either perspective, the design should be simple and not draw attention away from the texts. See uploaded PDF file "Examples.pdf"
For attendees at a Buddhist Event.

```html
<!DOCTYPE html>
<html lang="en">
<head>
<meta charset="utf-8">
<title>Pull-Up Banners · Ten Mistaking &amp; Desire and Attachment</title>
<link rel="stylesheet" href="https://fonts.googleapis.com/css2?family=Cabin+Condensed:wght@500&family=EB+Garamond:wght@400&family=Noto+Sans+SC:wght@300&family=Noto+Serif+Tibetan:wght@400&display=swap">
<style>
  :root {
    --crimson: #b3173c;
    --frame-green: #4fb84a;
    --frame-green-dark: #3a9e3a;
    --bg-top: #a6d99a;
    --bg-mid: #c3e39a;
    --bg-low: #e2da78;
    --bg-gold: #d9b44a;
    --card-top: #ffffff;
    --card-bottom: #f5eeb0;
    --plaque: #f4efc9;
    --white-line: #ffffff;
  }
  * { margin: 0; padding: 0; box-sizing: border-box; }
  html, body { width: 1200px; height: 1200px; overflow: hidden; background: #fff; }
  .canvas { position: relative; width: 1200px; height: 1200px; overflow: hidden; }
  .banner-field {
    position: absolute; top: 0; width: 600px; height: 1200px;
    background: linear-gradient(180deg, var(--bg-top) 0%, var(--bg-mid) 45%, var(--bg-low) 78%, var(--bg-gold) 100%);
  }
  .banner-field.left { left: 0; }
  .banner-field.right { left: 600px; }
  .outline { position: absolute; inset: 0; width: 1200px; height: 1200px; }
  .deity-emblem {
    position: absolute; width: 120px; height: 140px; border-radius: 50% 50% 10px 10px;
    background: radial-gradient(circle at 50% 45%, rgba(179,23,60,.35), rgba(179,23,60,.08) 70%);
  }
  .title {
    position: absolute; color: var(--crimson);
    font-family: "Cabin Condensed", sans-serif; font-weight: 500; line-height: 1; letter-spacing: -0.5px;
  }
  .inner-frame { position: absolute; border: 3px solid var(--frame-green); box-shadow: inset 0 0 0 1px rgba(255,255,255,.6); }
  .text-card {
    position: absolute;
    background: linear-gradient(180deg, var(--card-top) 0%, #fbf9e6 50%, var(--card-bottom) 100%);
    box-shadow: 0 0 4px rgba(0,0,0,.1);
  }
  .corner-mark {
    position: absolute; width: 50px; height: 50px;
    border: 3px solid var(--frame-green-dark); background: rgba(79,184,74,.12);
  }
  .divider { position: absolute; height: 3px; background: var(--frame-green); }
  .text-block { position: absolute; color: var(--crimson); text-align: center; }
  .tibetan { font-family: "Noto Serif Tibetan", serif; }
  .chinese { font-family: "Noto Sans SC", sans-serif; font-weight: 300; }
  .english { font-family: "EB Garamond", serif; }
  .plaque {
    position: absolute; background: var(--plaque); opacity: .92;
  }
  .plaque::after {
    content: ""; position: absolute; inset: 8px; border: 2px solid #d8cf98;
  }
  .plaque-text { position: absolute; left: 0; right: 0; text-align: center; color: var(--crimson); }
</style>
</head>
<body>
<div class="canvas">

  <div class="banner-field left" role="img" aria-label="Soft green-to-gold background with scattered bodhi leaves and a faint seated Buddha figure"></div>
  <div class="banner-field right" role="img" aria-label="Soft green-to-gold background with scattered bodhi leaves and a faint seated Buddha figure"></div>

  <svg class="outline" viewBox="0 0 1200 1200" aria-hidden="true">
    <path d="M84 14 H514 A68 68 0 0 0 582 82 V1116 A68 68 0 0 0 514 1184 H84 A68 68 0 0 0 16 1116 V82 A68 68 0 0 0 84 14 Z" fill="none" stroke="var(--white-line)" stroke-width="3"/>
    <path d="M686 12 H1120 A68 68 0 0 0 1188 80 V1120 A68 68 0 0 0 1120 1188 H686 A68 68 0 0 0 618 1120 V80 A68 68 0 0 0 686 12 Z" fill="none" stroke="var(--white-line)" stroke-width="3"/>
  </svg>

  <!-- Banner 1 -->
  <section class="banner-ten-mistaking">
    <div class="deity-emblem" style="left:80px;top:54px;" role="img" aria-label="Line drawing of a crowned deity on a lotus throne"></div>
    <h1 class="title" style="left:208px;top:92px;font-size:58px;">Ten Mistaking</h1>

    <div class="inner-frame" style="left:42px;top:222px;width:518px;height:752px;"></div>
    <div class="text-card" style="left:62px;top:244px;width:480px;height:708px;"></div>

    <div class="corner-mark" role="img" aria-label="Auspicious corner symbol" style="left:74px;top:256px;"></div>
    <div class="corner-mark" role="img" aria-label="Auspicious corner symbol" style="left:478px;top:256px;"></div>
    <div class="corner-mark" role="img" aria-label="Auspicious corner symbol" style="left:74px;top:882px;"></div>
    <div class="corner-mark" role="img" aria-label="Auspicious corner symbol" style="left:478px;top:882px;"></div>

    <div class="text-block tibetan" style="left:62px;width:480px;top:294px;font-size:10px;line-height:17.3px;">
      དད་པ་དང་འདུན་པ་ལ་ནོར་སླ།<br>
      བྱམས་སྙིང་རྗེ་དང་ཆགས་པ་ལ་ནོར་སླ།<br>
      ཤེས་བྱའི་གཤིས་ཀྱི་སྟོང་པ་དང་རྣམ་རྟོག་གི་སྟོང་པ་ལ་ནོར་སླ།<br>
      ཆོས་ཀྱི་དབྱིངས་དང་ཆད་ལྟ་ལ་ནོར་སླ།<br>
      ཉམས་མྱོང་དང་རྟོགས་པ་ལ་ནོར་སླ།<br>
      བཙུན་པ་དང་ཆོལ་འཚོང་བ་ལ་ནོར་སླ།<br>
      འཁྲུལ་ཞིག་དང་བདུད་འཛིན་ལ་ནོར་སླ།<br>
      གྲུབ་ཐོབ་དང་རྫུན་བཟོ་བ་ལ་ནོར་སླ།<br>
      གཞན་དོན་བྱེད་པ་དང་རང་དོན་བྱེད་པ་ལ་ནོར་སླ།<br>
      ཐབས་མཁས་པ་དང་གཡོ་སྒྱུ་ལ་ནོར་སླ།
    </div>

    <div class="divider" style="left:98px;width:406px;top:483px;"></div>

    <div class="text-block chinese" style="left:62px;width:480px;top:516px;font-size:13px;line-height:16.2px;">
      信心与爱欲可能混淆，<br>
      慈悲与贪执可能混淆，<br>
      所知¹本空与思维造作空性可能混淆，<br>
      法界与断见²可能混淆，<br>
      觉受与证悟可能混淆，<br>
      尊者与神棍可能混淆，<br>
      破惑与著魔可能混淆，<br>
      成就者与骗子可能混淆，<br>
      利他与自利可能混淆，<br>
      方便善巧与谄媚哄骗可能混淆。
    </div>
    <div class="text-block chinese" style="left:62px;width:480px;top:698px;font-size:5.5px;line-height:7px;">
      1．所知：可以认识的外境。<br>
      2．断见：否定因果、前生、后世等说法的见解
    </div>

    <div class="divider" style="left:98px;width:406px;top:724px;"></div>

    <div class="text-block english" style="left:62px;width:480px;top:752px;font-size:8.6px;line-height:15.2px;">
      Desire can be mistaken for faith or devotion.<br>
      Attachment can be mistaken for love and compassion.<br>
      Conceptual emptiness can be mistaken for the emptiness of the nature of phenomena.<br>
      Nihilism can be mistaken for the dharmadhatu.<br>
      A meditative experience can be mistaken for realization.<br>
      Outer religious practices can be mistaken for inner development of good qualities.<br>
      A person in the grip of a demon can be mistaken for a person who has destroyed his own delusions.<br>
      A charlatan can be mistaken for a siddha.<br>
      An act to benefit yourself can be mistaken for an act to benefit others.<br>
      Deviousness can be mistaken for skillful means.
    </div>

    <div class="plaque" style="left:120px;top:1000px;width:358px;height:140px;">
      <div class="plaque-text tibetan" style="top:30px;font-size:16px;">སྨོན་ལམ།  བསྔོ་བ་ཡོངས་རྫོགས།</div>
      <div class="plaque-text chinese" style="top:58px;font-size:19px;font-weight:400;">愿诸有情共证佛果位</div>
      <div class="plaque-text english" style="top:86px;font-size:19px;">May all attain Buddhahood together.</div>
    </div>
  </section>

  <!-- Banner 2 -->
  <section class="banner-desire-attachment">
    <div class="deity-emblem" style="left:684px;top:54px;" role="img" aria-label="Line drawing of a crowned deity on a lotus throne"></div>
    <h1 class="title" style="left:884px;top:68px;font-size:58px;">Desire <span style="font-size:40px;">&amp;</span></h1>
    <div class="title" style="left:836px;top:124px;font-size:62px;">Attachment</div>

    <div class="inner-frame" style="left:642px;top:220px;width:522px;height:758px;"></div>
    <div class="text-card" style="left:662px;top:244px;width:480px;height:708px;"></div>

    <div class="corner-mark" role="img" aria-label="Auspicious corner symbol" style="left:672px;top:254px;"></div>
    <div class="corner-mark" role="img" aria-label="Auspicious corner symbol" style="left:1080px;top:254px;"></div>
    <div class="corner-mark" role="img" aria-label="Auspicious corner symbol" style="left:672px;top:884px;"></div>
    <div class="corner-mark" role="img" aria-label="Auspicious corner symbol" style="left:1080px;top:884px;"></div>

    <div class="text-block tibetan" style="left:740px;width:400px;top:304px;font-size:17px;line-height:37px;text-align:left;">
      འདུན་པ་མེད་ན་རང་དོན་མི་འགྲུབ་ཅིང་།<br>
      འདུན་པ་ཡོད་ཚད་ཆགས་པ་མ་ཡིན་པས།<br>
      འདུན་དང་ཆགས་པའི་ཁྱད་པར་མ་ཤེས་པར།<br>
      འདོད་ཆགས་ལམ་དུ་སློང་བ་ཞེས་པ་རྨོངས།
    </div>

    <div class="divider" style="left:698px;width:408px;top:483px;"></div>

    <div class="text-block chinese" style="left:756px;width:400px;top:526px;font-size:29px;line-height:36px;text-align:left;">
      若无意欲则不成自利，<br>
      然有意欲非为执着故，<br>
      不知意欲执着差别即，<br>
      贪执说所当取确荒唐
    </div>

    <div class="divider" style="left:698px;width:408px;top:725px;"></div>

    <div class="text-block english" style="left:662px;width:480px;top:748px;font-size:14px;line-height:32px;">
      If you have no desire, your goal cannot be achieved.<br>
      Since not all desire is attachment,<br>
      not knowing how to differentiate desire from attachment,<br>
      to talk about bringing passion into the path is absurd.
    </div>

    <div class="plaque" style="left:724px;top:1004px;width:358px;height:140px;">
      <div class="plaque-text tibetan" style="top:30px;font-size:16px;">སྨོན་ལམ།  བསྔོ་བ་ཡོངས་རྫོགས།</div>
      <div class="plaque-text chinese" style="top:58px;font-size:19px;font-weight:400;">愿诸有情共证佛果位</div>
      <div class="plaque-text english" style="top:86px;font-size:19px;">May all attain Buddhahood together.</div>
    </div>
  </section>

</div>
</body>
</html>
```